Refresh of graphic design for existing website

We would like to refresh our website. Please see the attached design specifications.

Industry/Entity Type

Graphic Design

```html
<!DOCTYPE html>
<html lang="en">
<head>
<meta charset="utf-8">
<title>The Garage Gear Institute</title>
<link rel="stylesheet" href="https://fonts.googleapis.com/css2?family=Roboto:wght@400;500;700&display=swap">
<style>
:root{
  --brand:#1a4fa0;
  --brand-dark:#0e347a;
  --brand-light:#2f7fd8;
  --ink:#333;
  --muted:#666;
  --line:#d6d6d6;
  --footer:#2c2c2c;
  --footer-text:#bdbdbd;
  --white:#fff;
}
*{box-sizing:border-box;margin:0;padding:0}
html,body{width:742px;height:1200px;overflow:hidden}
body{font-family:"Roboto",Arial,sans-serif;color:var(--ink);background:var(--white);position:relative}
.site-header{height:44px;display:flex;align-items:center;justify-content:space-between;padding:0 12px}
.brand{display:flex;align-items:center;gap:6px;font-weight:700;font-size:22px;color:var(--brand)}
.brand-dot{width:14px;height:14px;border-radius:50%;background:var(--brand-light)}
.header-tools{display:flex;align-items:center;gap:6px}
.search-field{width:128px;height:20px;border:1px solid var(--line);font-size:8px;color:#999;padding:5px 6px}
.login-btn{height:20px;padding:0 12px;background:var(--brand-dark);color:var(--white);font-size:9px;font-weight:500;display:flex;align-items:center}
.social{display:flex;gap:4px}
.social span{width:14px;height:14px;border-radius:50%;background:var(--brand)}
.main-nav{height:18px;background:var(--brand-dark);display:flex;align-items:center;padding:0 12px;gap:21px}
.main-nav a{color:var(--white);font-size:7.5px;font-weight:500;text-decoration:none;letter-spacing:.2px}
.main-nav .nav-search{margin-left:auto;width:14px;height:14px;border-radius:50%;background:var(--brand-light)}
.hero{position:absolute;top:62px;left:0;width:742px;height:408px}
.hero-photo{position:absolute;inset:0;background:linear-gradient(100deg,#5b6470 0%,#8c949c 30%,#b8bdc2 55%,#d8d4cc 75%,#6f7a86 100%)}
.hero-title{position:absolute;left:40px;top:292px;color:var(--white);font-size:24px;font-weight:700}
.hero-sub{position:absolute;left:40px;top:326px;background:rgba(26,79,160,.85);color:var(--white);font-size:14px;padding:7px 14px}
.hero-arrow{position:absolute;top:190px;width:14px;height:28px;background:rgba(0,0,0,.55)}
.hero-arrow.prev{left:0}.hero-arrow.next{right:0}
.hero-arrow svg{display:block;margin:8px auto}
.section-title{text-align:center;font-size:16px;font-weight:700;color:#222}
.section-title::after{content:"";display:block;width:30px;height:2px;background:var(--brand);margin:5px auto 0}
.about{position:absolute;top:480px;left:0;width:742px}
.about p{width:640px;margin:12px auto 0;font-size:8px;line-height:14px;color:var(--muted);text-align:center}
.events{position:absolute;top:625px;left:0;width:742px}
.event-list{display:flex;justify-content:center;gap:34px;margin-top:20px}
.event-card{width:196px}
.event-photo{position:relative;height:130px}
.event-date{position:absolute;right:0;bottom:0;background:var(--brand);color:var(--white);font-size:8px;padding:4px 6px}
.event-card h3{font-size:9px;font-weight:700;margin-top:7px;color:#222}
.event-card p{font-size:8px;color:var(--muted);margin-top:3px}
.news{position:absolute;top:868px;left:0;width:742px;height:207px;background:var(--brand);color:var(--white);padding-top:12px}
.news .section-title{color:var(--white)}
.news .section-title::after{background:var(--white)}
.news-intro{width:640px;margin:8px auto 0;font-size:8px;line-height:13px;text-align:center;color:#dce6f5}
.news-grid{display:grid;grid-template-columns:1fr 1fr;gap:12px 40px;width:640px;margin:14px auto 0}
.news-item{display:flex;gap:10px;border-bottom:1px solid rgba(255,255,255,.3);padding-bottom:8px}
.news-num{flex:none;width:22px;height:22px;background:var(--white);color:var(--brand);font-size:11px;font-weight:700;display:flex;align-items:center;justify-content:center}
.news-body time{display:block;text-align:right;font-size:7px;color:#dce6f5}
.news-body p{font-size:7.5px;line-height:11px}
.site-footer{position:absolute;top:1075px;left:0;width:742px;height:110px;background:var(--footer);display:flex;padding:10px 30px 0;gap:26px}
.footer-col h4{color:var(--brand-light);font-size:10px;font-weight:500;margin-bottom:5px}
.footer-col p,.footer-col li{font-size:7px;line-height:11px;color:var(--footer-text);list-style:none}
.col-about{width:190px}.col-menu{width:80px}.col-links{width:110px}.col-blog{width:180px}
.blog-post{display:flex;gap:6px;margin-bottom:5px}
.blog-thumb{width:22px;height:18px;flex:none}
.copyright{position:absolute;top:1185px;left:0;width:742px;height:15px;background:var(--brand-dark);color:#dce6f5;font-size:7px;text-align:center;line-height:15px}
</style>
</head>
<body>
<header class="site-header">
  <div class="brand"><span class="brand-dot"></span>GGI</div>
  <div class="header-tools">
    <div class="search-field">Search</div>
    <div class="login-btn">Login</div>
    <div class="social"><span></span><span></span><span></span><span></span></div>
  </div>
</header>
<nav class="main-nav">
  <a href="#">HOME</a><a href="#">ABOUT GGI</a><a href="#">MEMBERSHIP</a><a href="#">GGI MEMBERS</a><a href="#">GGI EVENTS</a><a href="#">TECH-DOC LIBRARY</a><a href="#">MARKET RESEARCH</a><a href="#">CONTACT US</a>
  <span class="nav-search"></span>
</nav>

<section class="hero">
  <div class="hero-photo" role="img" aria-label="Smiling mechanic in a blue cap and work shirt holding a clipboard in a repair garage"></div>
  <div class="hero-arrow prev"><svg width="6" height="10"><path d="M5 1 1 5l4 4" stroke="#fff" fill="none" stroke-width="1.5"/></svg></div>
  <div class="hero-arrow next"><svg width="6" height="10"><path d="M1 1l4 4-4 4" stroke="#fff" fill="none" stroke-width="1.5"/></svg></div>
  <h1 class="hero-title">The Garage Gear Institute</h1>
  <div class="hero-sub">Serving the Automotive Repair Industry Since 1947</div>
</section>

<section class="about">
  <h2 class="section-title">About GGI</h2>
  <p>Lorem ipsum dolor sit amet, consectetur adipiscing elit, sed do eiusmod tempor incididunt ut labore et dolore magna aliqua. Ut enim ad minim veniam, quis nostrud exercitation ullamco laboris nisi ut aliquip ex ea commodo consequat. Duis aute irure dolor in reprehenderit in voluptate velit esse cillum dolore eu fugiat nulla pariatur. Excepteur sint occaecat cupidatat non proident, sunt in culpa qui officia deserunt mollit anim id est laborum. Sed ut perspiciatis unde omnis iste natus error sit voluptatem accusantium doloremque laudantium, totam rem aperiam, eaque ipsa quae ab illo inventore veritatis et quasi architecto beatae vitae dicta sunt explicabo. Nemo enim ipsam voluptatem quia voluptas sit aspernatur aut odit aut fugit.</p>
</section>

<section class="events">
  <h2 class="section-title">Upcomming Events</h2>
  <div class="event-list">
    <article class="event-card">
      <div class="event-photo" role="img" aria-label="Mechanic working on an engine bay" style="background:linear-gradient(135deg,#4a5560,#a7adb3)"><span class="event-date">16 Jan</span></div>
      <h3>Lorem Ipsum is simply dummy text</h3><p>Las Vegas, CA</p>
    </article>
    <article class="event-card">
      <div class="event-photo" role="img" aria-label="Close view of tools on an engine" style="background:linear-gradient(135deg,#2f3338,#8a8f94)"><span class="event-date">16 Jan</span></div>
      <h3>Lorem Ipsum is simply dummy text</h3><p>Las Vegas, CA</p>
    </article>
    <article class="event-card">
      <div class="event-photo" role="img" aria-label="Auto repair shop exterior with a red sign" style="background:linear-gradient(135deg,#a33a32,#c9c3b8 60%,#7d8ea3)"><span class="event-date">16 Jan</span></div>
      <h3>Lorem Ipsum is simply dummy text</h3><p>Las Vegas, CA</p>
    </article>
  </div>
</section>

<section class="news">
  <h2 class="section-title">Industry News</h2>
  <p class="news-intro">Lorem Ipsum is simply dummy text of the printing and typesetting industry. Lorem Ipsum has been the industry's standard dummy text ever since the 1500s, when an unknown printer took a galley of type and scrambled it to make a type specimen book. Lorem Ipsum is not simply random text.</p>
  <div class="news-grid">
    <div class="news-item"><span class="news-num">1</span><div class="news-body"><time>11 Sep 2016</time><p>The standard chunk of Lorem Ipsum used since the 1500s is reproduced below for those interested. Sections 1.10.32 and 1.10.33 are also here.</p></div></div>
    <div class="news-item"><span class="news-num">3</span><div class="news-body"><time>11 Sep 2016</time><p>The standard chunk of Lorem Ipsum used since the 1500s is reproduced below for those interested. Sections 1.10.32 and 1.10.33 are also here.</p></div></div>
    <div class="news-item"><span class="news-num">2</span><div class="news-body"><time>11 Sep 2016</time><p>The standard chunk of Lorem Ipsum used since the 1500s is reproduced below for those interested. Sections 1.10.32 and 1.10.33 are also here.</p></div></div>
    <div class="news-item"><span class="news-num">4</span><div class="news-body"><time>11 Sep 2016</time><p>The standard chunk of Lorem Ipsum used since the 1500s is reproduced below for those interested. Sections 1.10.32 and 1.10.33 are also here.</p></div></div>
  </div>
</section>

<footer class="site-footer">
  <div class="footer-col col-about">
    <h4>Join GGI</h4>
    <p>The standard chunk of Lorem Ipsum used since the 1500s is reproduced below for those interested. Sections 1.10.32 and 1.10.33 are also reproduced in their exact original form, accompanied by a plain English version.</p>
  </div>
  <div class="footer-col col-menu">
    <h4>Menu</h4>
    <ul><li>About</li><li>FAQ</li><li>Contact</li><li>Terms</li><li>Privacy</li></ul>
  </div>
  <div class="footer-col col-links">
    <h4>Quick Links</h4>
    <ul><li>TECH-DOC Library</li><li>GGI Board Mtg</li><li>GGI Events</li><li>Contact Center</li><li>Partnership</li><li>GGI Market Research</li><li>Advertise</li></ul>
  </div>
  <div class="footer-col col-blog">
    <h4>GGI Blog</h4>
    <div class="blog-post"><span class="blog-thumb" role="img" aria-label="Workshop photo" style="background:#6d7782"></span><p>Lorem ipsum dolor sit amet, lorem adipiscing elit.</p></div>
    <div class="blog-post"><span class="blog-thumb" role="img" aria-label="Tools photo" style="background:#8b7a6a"></span><p>Lorem ipsum dolor sit amet, lorem adipiscing elit.</p></div>
    <div class="blog-post"><span class="blog-thumb" role="img" aria-label="Garage photo" style="background:#5a6b80"></span><p>Lorem ipsum dolor sit amet, lorem adipiscing elit.</p></div>
  </div>
</footer>
<div class="copyright">Garage Gear Institute Copyright 2016</div>
</body>
</html>
```